New Business Card Design for TPR

A new business card design with our current logo and information. I need an editable version in .ai format. Here is a general layout, and needs a new fresh face. This is of course in the Horticulture Lighting Industry. No hemp or canna graphics or images. This is a fast growing professional company, so I need a design that reflects this feel. I want an original design. If you have any questions, please let me know. Attached is front and back and one additional logo that can be used.

```html
<!DOCTYPE html>
<html lang="en">
<head>
<meta charset="utf-8">
<title>TPR Business Card</title>
<link href="https://fonts.googleapis.com/css2?family=Montserrat:wght@400;500;700&display=swap" rel="stylesheet">
<style>
  :root {
    --bg: #d9dadb;
    --card: #121212;
    --card-hi: #2a2a2a;
    --green: #3fae2a;
    --lime: #b9d232;
    --white: #f2f2f2;
    --leaf: #1e1e1e;
  }
  * { margin: 0; padding: 0; box-sizing: border-box; }
  html, body { width: 1200px; height: 900px; overflow: hidden; }
  body {
    background: var(--bg);
    font-family: "Montserrat", sans-serif;
    position: relative;
  }
  .card {
    position: absolute;
    width: 640px;
    height: 366px;
    border-radius: 22px;
    background: linear-gradient(135deg, var(--card-hi) 0%, var(--card) 45%, var(--card) 100%);
    border-bottom: 7px solid var(--green);
    overflow: hidden;
  }
  .card--front { left: 60px; top: 60px; }
  .card--back { left: 500px; top: 474px; }

  .leaf-decor { position: absolute; }
  .card--front .leaf-decor {
    left: 0; top: 60px; width: 380px; height: 300px;
    background: radial-gradient(ellipse at 40% 60%, #2c2c2c 0%, var(--leaf) 45%, transparent 75%);
  }
  .card--back .leaf-decor {
    right: 0; top: 0; width: 420px; height: 300px;
    background: radial-gradient(ellipse at 60% 45%, #2b2b2b 0%, var(--leaf) 45%, transparent 75%);
  }

  .brand {
    position: absolute;
    display: flex;
    align-items: center;
    gap: 12px;
  }
  .brand__square {
    width: 18px; height: 18px;
    background: var(--green);
    flex: none;
  }
  .brand__name {
    color: var(--green);
    font-weight: 700;
    font-size: 30px;
    line-height: 1;
    white-space: nowrap;
  }
  .card--front .brand { left: 300px; top: 172px; }
  .card--back .brand { left: 40px; top: 62px; }
  .card--back .brand__square { width: 15px; height: 15px; }
  .card--back .brand__name { font-size: 24px; }

  .person { position: absolute; left: 40px; top: 136px; }
  .person__name { color: var(--green); font-weight: 700; font-size: 24px; }
  .person__role { color: var(--lime); font-weight: 400; font-size: 14px; margin-top: 2px; }

  .address {
    position: absolute; left: 40px; top: 206px;
    color: var(--white); font-size: 15px; line-height: 1.3;
  }
  .contacts {
    position: absolute; left: 40px; top: 262px;
    list-style: none; color: var(--white); font-size: 15px;
  }
  .contacts li { display: flex; align-items: center; gap: 10px; height: 26px; }
  .contacts svg { width: 14px; height: 14px; flex: none; }
  .icon-fill { fill: var(--green); }
  .icon-line { fill: none; stroke: var(--green); stroke-width: 1.6; }
</style>
</head>
<body>

<section class="card card--front" aria-label="Card front">
  <div class="leaf-decor" role="img" aria-label="Subtle embossed leaf shapes"></div>
  <div class="brand">
    <div class="brand__square"></div>
    <div class="brand__name">TPR Grow Lighting</div>
  </div>
</section>

<section class="card card--back" aria-label="Card back">
  <div class="leaf-decor" role="img" aria-label="Subtle embossed leaf shapes"></div>
  <div class="brand">
    <div class="brand__square"></div>
    <div class="brand__name">TPR Grow Lighting</div>
  </div>
  <div class="person">
    <div class="person__name">Daniel Hale</div>
    <div class="person__role">Owner</div>
  </div>
  <p class="address">Here is your full address<br>Road no.45, Austin, USA</p>
  <ul class="contacts">
    <li>
      <svg viewBox="0 0 16 16" aria-hidden="true"><path class="icon-fill" d="M3 1h3l1.5 4-2 1.2a9 9 0 0 0 4.3 4.3L11 8.5l4 1.5v3a2 2 0 0 1-2 2A12 12 0 0 1 1 3a2 2 0 0 1 2-2z"/></svg>
      555-014-2876
    </li>
    <li>
      <svg viewBox="0 0 16 16" aria-hidden="true"><rect class="icon-line" x="1.5" y="3.5" width="13" height="9"/><path class="icon-line" d="M1.5 3.5l6.5 5.5 6.5-5.5"/></svg>
      info@tprgrowlight.com
    </li>
    <li>
      <svg viewBox="0 0 16 16" aria-hidden="true"><circle class="icon-line" cx="8" cy="8" r="6.5"/><path class="icon-line" d="M1.5 8h13M8 1.5c-3 3.5-3 9.5 0 13M8 1.5c3 3.5 3 9.5 0 13"/></svg>
      www.tprgrowlight.com
    </li>
  </ul>
</section>

</body>
</html>
```